Email Signature - GRAND HARBOUR STAYS DIRECT

Hi there,

I'm after an email signature for my email. I have attached a sample of what I like to this brief (File name: "Email Signature Sample").

I would like my email signature to have the following information:

Delphine Worrow
GRAND HARBOUR STAYS DIRECT
Mobile: 0431 792 046 ( Australia )
Tel: +61 431 792 046 ( International )
Email: delphine@grandharbourstaysdirect.example
Website: www.grandharbourstaysdirectexample

Industry/Entity Type

Online

Requirements
Must have
• I would like the signature to have a professional look

```html
<!DOCTYPE html>
<html lang="en">
<head>
<meta charset="utf-8">
<title>Delphine Worrow — Grand Harbour Stays Direct</title>
<link href="https://fonts.googleapis.com/css2?family=Source+Sans+3:wght@400;600;700&display=swap" rel="stylesheet">
<style>
  :root {
    --page: #ffffff;
    --card: #ffffff;
    --card-border: #111111;
    --card-shadow: #565656;
    --accent-red: #e8432f;
    --link-red: #e8221b;
    --company-grey: #555555;
    --ink-navy: #2a2f6b;
    --stripe-green: #3cb54a;
    --stripe-orange: #f05a28;
  }
  * { margin: 0; padding: 0; box-sizing: border-box; }
  html, body {
    width: 1200px; height: 1000px; overflow: hidden;
    background: var(--page);
    font-family: "Source Sans 3", sans-serif;
  }
  .canvas { position: relative; width: 1200px; height: 1000px; }
  .signature-shadow {
    position: absolute; left: 305px; top: 333px; width: 601px; height: 344px;
    background: var(--card-shadow);
  }
  .signature-card {
    position: absolute; left: 295px; top: 323px; width: 602px; height: 345px;
    background: var(--card); border: 2px solid var(--card-border);
  }
  .corner-stripes { position: absolute; left: 0; top: 0; }
  .person-name {
    position: absolute; left: 39px; top: 64px;
    font-size: 30px; font-weight: 600; letter-spacing: 0.3px;
    color: var(--accent-red); line-height: 1;
  }
  .name-rule {
    position: absolute; left: 39px; top: 101px; width: 250px; height: 2px;
    background: var(--accent-red);
  }
  .company-name {
    position: absolute; left: 39px; top: 110px;
    font-size: 14px; font-weight: 700; color: var(--company-grey); line-height: 1;
  }
  .contact-list { position: absolute; left: 39px; top: 0; list-style: none; }
  .contact-item {
    position: absolute; left: 0; display: flex; align-items: center;
    white-space: nowrap; color: var(--ink-navy);
  }
  .contact-icon { width: 18px; height: 18px; margin-right: 12px; flex: none; }
  .contact-item.mobile { top: 201px; font-size: 16px; font-weight: 600; }
  .contact-item.tel { top: 231px; font-size: 15px; font-weight: 600; }
  .contact-item.email { top: 259px; font-size: 19px; font-weight: 400; }
  .contact-item.web { top: 288px; font-size: 19px; font-weight: 400; }
  .note { font-size: 0.9em; }
  .web-domain { color: var(--link-red); font-weight: 700; }
</style>
</head>
<body>
<div class="canvas">
  <div class="signature-shadow"></div>
  <div class="signature-card">
    <svg class="corner-stripes" width="600" height="343" viewBox="0 0 600 343" aria-hidden="true">
      <polygon points="434,8 481,8 588,115 588,163" fill="var(--stripe-green)"/>
      <polygon points="500,8 548,8 589,49 589,97" fill="var(--stripe-orange)"/>
    </svg>

    <h1 class="person-name">DELPHINE WORROW</h1>
    <div class="name-rule"></div>
    <p class="company-name">GRAND HARBOUR STAYS DIRECT</p>

    <ul class="contact-list">
      <li class="contact-item mobile">
        <svg class="contact-icon" viewBox="0 0 18 18" aria-hidden="true">
          <rect x="3" y="2" width="12" height="16" rx="2.5" fill="var(--ink-navy)"/>
          <rect x="3.8" y="0" width="1.6" height="3" fill="var(--ink-navy)"/>
          <rect x="5.5" y="5" width="7" height="4.5" rx="0.8" fill="#fff"/>
          <circle cx="9" cy="14" r="1" fill="#fff"/>
        </svg>
        0431 792 046&nbsp;<span class="note">( Australia )</span>
      </li>
      <li class="contact-item tel">
        <svg class="contact-icon" viewBox="0 0 18 18" aria-hidden="true">
          <rect x="0" y="0" width="18" height="18" rx="3" fill="var(--ink-navy)"/>
          <path d="M6 3.5 L8 3.5 L8.5 6.5 L7.2 7.3 C7.8 9.5 9 11 10.5 11.8 L11.5 10.6 L14 11.5 L14 13.8 C9 14.2 4.5 9 5 4.5 Z" fill="#fff"/>
        </svg>
        +61 431 792 046&nbsp;<span class="note">( International )</span>
      </li>
      <li class="contact-item email">
        <svg class="contact-icon" viewBox="0 0 18 18" aria-hidden="true">
          <rect x="1" y="3.5" width="16" height="11" fill="none" stroke="var(--ink-navy)" stroke-width="1.6"/>
          <path d="M1 3.5 L9 10 L17 3.5 M1 14.5 L7 8.5 M17 14.5 L11 8.5" fill="none" stroke="var(--ink-navy)" stroke-width="1.4"/>
        </svg>
        delphine@grandharbourstaysdirect.example
      </li>
      <li class="contact-item web">
        <svg class="contact-icon" viewBox="0 0 18 18" aria-hidden="true">
          <circle cx="8.5" cy="8.5" r="7.5" fill="var(--ink-navy)"/>
          <path d="M1.5 8.5 H15.5 M8.5 1 V16 M3 4.5 H14 M3 12.5 H14" stroke="#fff" stroke-width="1"/>
          <ellipse cx="8.5" cy="8.5" rx="3.3" ry="7.5" fill="none" stroke="#fff" stroke-width="1"/>
          <path d="M10 9 L10 18 L12.2 15.8 L14 18 L15.3 17 L13.6 14.8 L16.5 14.5 Z" fill="var(--ink-navy)" stroke="#fff" stroke-width="0.9"/>
        </svg>
        www.<span class="web-domain">grandharbourstaysdirect</span>.example
      </li>
    </ul>
  </div>
</div>
</body>
</html>
```